Flyer for Photo booth business for wedding expo

Hi the flyer is for sunny moments selfie stand rentals.
We are wanting a flyer for a wedding expo this weekend.

1 sided A4

Check out our website for colours etc www.brightsnapstand.example.au

We are offering 10% discount on Platinum Packages for bookings confirmed within two weeks of the Bridal expo.

Expo Engagement party and Wedding package $1,900.00

Savings of $320.00

3 hour photo booth hire for Engagement package with the funky retro party booth including Props and Logo.

4 hour Platinum Wedding package with Video messaging.

We have a logos and images for the brochure, we are looking for a sleek and fun design with the sunny moments colours.

www.brightsnapstand.example.au
info@brightsnapstand.example.au
0400 123 456

Target Market(s)

potential bride and grooms. partys weddings

Industry/Entity Type

Wedding

Requirements
Must have
• logo and wedding feel
Nice to have
• inventive and creative layout

```html
<!DOCTYPE html>
<html lang="en">
<head>
<meta charset="utf-8">
<title>Sunny Moments – Bridal Expo Flyer</title>
<link href="https://fonts.googleapis.com/css2?family=Arimo:wght@700&family=Roboto+Condensed:wght@400;700;800&display=swap" rel="stylesheet">
<style>
  :root{
    --ink:#14110e;
    --ink-soft:#1f1a15;
    --film:#e6d6a4;
    --film-dark:#241a11;
    --sepia-light:#e0a95e;
    --sepia-mid:#9a5a22;
    --sepia-deep:#3b2210;
    --yellow:#f3e500;
    --orange:#f7941d;
    --white:#ffffff;
  }
  *{margin:0;padding:0;box-sizing:border-box}
  html,body{width:844px;height:1200px;overflow:hidden;background:var(--ink)}
  body{font-family:"Roboto Condensed",Arial,sans-serif}
  .flyer{position:relative;width:844px;height:1200px;background:var(--ink);overflow:hidden}

  /* top film frame */
  .film-top{position:absolute;left:0;top:0;width:844px;height:400px;background:var(--film)}
  .film-top svg{position:absolute;left:0;top:0}
  .hero-photo{position:absolute;top:47px;height:293px;border-radius:12px;
    background:radial-gradient(ellipse at 50% 40%,var(--sepia-light),var(--sepia-mid) 55%,var(--sepia-deep) 95%)}
  .hero-photo.left{left:24px;width:400px}
  .hero-photo.right{left:427px;width:392px}

  /* offer copy */
  .offer{position:absolute;left:0;top:400px;width:844px;height:480px;text-align:center;
    background:radial-gradient(ellipse at 50% 40%,var(--ink-soft),var(--ink) 75%)}
  .headline-percent{position:absolute;left:0;width:100%;top:20px;font-family:"Arimo",Arial,sans-serif;font-size:62px;font-weight:700;color:var(--yellow);line-height:70px}
  .discount-terms{position:absolute;left:0;width:100%;top:95px;color:var(--orange);font-weight:700;font-size:18px;line-height:24px;letter-spacing:1.5px}
  .package-title{position:absolute;left:0;width:100%;top:183px;color:var(--yellow);font-weight:700;font-size:30px;line-height:40px;letter-spacing:.6px}
  .package-saving{position:absolute;left:0;width:100%;top:262px;color:var(--yellow);font-weight:700;font-size:15px}
  .feature{position:absolute;display:flex;align-items:center;gap:12px}
  .feature-hours{color:var(--yellow);font-weight:800;font-size:34px;letter-spacing:.5px;white-space:nowrap}
  .feature-text{color:var(--orange);font-weight:700;font-size:14px;line-height:26px;text-align:left;letter-spacing:.6px;white-space:nowrap}
  .feature.engagement{left:136px;top:300px}
  .feature.wedding{left:181px;top:360px}
  .contact{position:absolute;left:273px;top:420px;width:334px;height:67px;background:#000;
    color:var(--yellow);font-weight:700;font-size:20px;line-height:24px;padding-top:10px;letter-spacing:.3px}

  /* bottom film collage */
  .film-bottom{position:absolute;left:0;top:880px;width:844px;height:320px;background:var(--film-dark)}
  .film-bottom svg{position:absolute;left:0;top:0}
  .brand-mark{position:absolute;left:304px;top:1113px;width:243px;height:87px;background:var(--ink-soft);
    display:flex;align-items:center;justify-content:center;gap:10px}
  .brand-dot{width:20px;height:20px;border-radius:50%;background:var(--yellow)}
  .brand-name{color:var(--white);font-weight:700;font-size:27px}
</style>
</head>
<body>
<main class="flyer">

  <section class="film-top">
    <svg width="844" height="400" aria-hidden="true">
      <defs>
        <pattern id="sprocket" width="44" height="26" patternUnits="userSpaceOnUse">
          <rect x="10" y="4" width="24" height="16" rx="2" fill="var(--film-dark)"/>
        </pattern>
      </defs>
      <rect x="0" y="4" width="844" height="26" fill="url(#sprocket)"/>
      <rect x="12" y="36" width="820" height="316" fill="var(--film-dark)"/>
      <rect x="0" y="360" width="844" height="26" fill="url(#sprocket)"/>
    </svg>
    <div class="hero-photo left" role="img" aria-label="Sepia photo booth shot of a smiling couple wearing shutter shades and holding a clapperboard"></div>
    <div class="hero-photo right" role="img" aria-label="Mirrored sepia photo booth shot of the same couple with props"></div>
  </section>

  <section class="offer">
    <div class="headline-percent">10%</div>
    <p class="discount-terms">DISCOUNT ON PLATINUM PACKAGES<br>FOR BOOKINGS CONFIRMED<br>WITHIN TWO WEEKS OF THE BRIDAL EXPO</p>
    <h2 class="package-title">EXPO ENGAGEMENT<br>PARTY AND WEDDING PACKAGE $ 1,900.00</h2>
    <p class="package-saving">( Savings of $320.00 )</p>
    <div class="feature engagement">
      <span class="feature-hours">3 HOUR</span>
      <span class="feature-text">PHOTO BOOTH HIRE FOR ENGAGEMENT PACKAGE<br>WITH THE FUNKY RETRO PARTY BOOTH INCLUDING PROPS AND LOGO</span>
    </div>
    <div class="feature wedding">
      <span class="feature-hours">4 HOUR</span>
      <span class="feature-text">PLATINUM WEDDING PACKAGE WITH VIDEO MESSAGING</span>
    </div>
    <div class="contact">info@brightsnapstand.example.au<br>0400 123 456</div>
  </section>

  <section class="film-bottom">
    <svg width="844" height="320" role="img" aria-label="Overlapping angled sepia film strips showing guests posing with party props in the photo booth">
      <defs>
        <pattern id="holes" width="34" height="24" patternUnits="userSpaceOnUse">
          <rect x="7" y="5" width="20" height="14" rx="2" fill="var(--film)"/>
        </pattern>
        <radialGradient id="frame-warm" cx="50%" cy="40%" r="70%">
          <stop offset="0" stop-color="var(--sepia-light)"/>
          <stop offset=".6" stop-color="var(--sepia-mid)"/>
          <stop offset="1" stop-color="var(--sepia-deep)"/>
        </radialGradient>
        <radialGradient id="frame-dim" cx="45%" cy="45%" r="75%">
          <stop offset="0" stop-color="#c98a45"/>
          <stop offset=".65" stop-color="#7a431a"/>
          <stop offset="1" stop-color="#2e1a0c"/>
        </radialGradient>
      </defs>

      <g class="strip strip-left" transform="rotate(-4 150 160)">
        <rect x="-40" y="-4" width="330" height="300" fill="var(--film-dark)"/>
        <rect x="-40" y="2" width="330" height="24" fill="url(#holes)"/>
        <rect x="-30" y="34" width="140" height="226" fill="url(#frame-warm)"/>
        <rect x="116" y="34" width="166" height="226" fill="url(#frame-dim)"/>
        <rect x="-40" y="266" width="330" height="24" fill="url(#holes)"/>
      </g>

      <g class="strip strip-middle" transform="rotate(3 430 170)">
        <rect x="262" y="8" width="330" height="310" fill="var(--film-dark)"/>
        <rect x="262" y="14" width="330" height="24" fill="url(#holes)"/>
        <rect x="272" y="46" width="150" height="240" fill="url(#frame-dim)"/>
        <rect x="428" y="46" width="154" height="240" fill="url(#frame-warm)"/>
      </g>

      <g class="strip strip-right" transform="rotate(-9 700 150)">
        <rect x="560" y="-20" width="330" height="320" fill="var(--film-dark)"/>
        <rect x="560" y="-14" width="330" height="24" fill="url(#holes)"/>
        <rect x="570" y="18" width="150" height="250" fill="url(#frame-warm)"/>
        <rect x="726" y="18" width="160" height="250" fill="url(#frame-dim)"/>
        <rect x="560" y="272" width="330" height="24" fill="url(#holes)"/>
      </g>

      <rect x="0" y="262" width="844" height="36" fill="var(--film-dark)"/>
      <rect x="0" y="268" width="844" height="24" fill="url(#holes)"/>
      <rect x="0" y="298" width="844" height="22" fill="#c9b27c"/>
    </svg>
  </section>

  <div class="brand-mark">
    <span class="brand-dot"></span>
    <span class="brand-name">Sunny Moments</span>
  </div>

</main>
</body>
</html>
```